保証書としての安心感や高級感が第一です。
箔押しなどの特色印刷はしませんので、通常のフライヤーカラー印刷で可能な範囲で
お願いします。バックに地紋のようなものもOKです。
枠部分は保証書や表彰状などのよくある形で枠取りをお願いできると思います。
記載項目
下記の文言に弊社社名と落款角印(赤色)をお願いします。
飾り処サクヤ
株式会社 樫井 印

人形修理保証書
お買い上げの御人形はお客様に十分ご満足いただけます
よう細心の注意を払っおります。万一、人形に不具合が
下記の条件に従って保証致します。

1,修理保証期間
ご購入より5年間

保証番号

受注番号

お買い上げ日時

購入者氏名

購入者住所

2 保証内容
保証期間中、日本国内で正常な使用で過失なく人形本体部分
(お顔、髪の毛、胴体、手足、人形の持ち物道具)に不具合が
生じた場合最大2回まで下記の割合で費用保証します。
a. 対象商品が修理可能な場合.........
下記に定める割合と額を限度とした修理費用
b. 対象商品が修理不可能な場合.......
下記に基づく限度額の代替品の提供を保証

保証補償割合(保証限度額はいずれも実質購入金額を上限とします)
購入日より1年未満     修理金額(税別)の100%
購入日より1年以上2年未満 修理金額(税別)の50%
購入日より2年以上3年未満 修理金額(税別)の40%
購入日より3年以上4年未満 修理金額(税別)の30%
購入日より4年以上5年未満 修理金額(税別)の20%
3保証適用除外事項項目

1. 保証期間を過ぎて発生した損害。
2. 故意や重過失、差押えによる損害。
3. 火事、地震、洪水、津波、などの天災による損害。
4. 水濡れや湿気、カビ等による保管状況による劣化の損害。
5. 錆、変色、擦傷、劣化等、通常の使用による自然消耗で発生した損害。
6.「付属品」(ガラスケース、お道具、飾り台、屏風、親王台、お花、屏風、芯木など人形自体以外の、付属品または構成品に分けられる部分に生じた損害7
7. 製品を無断で改造もしくは修理したことが原因となって生じた損害。
8. 日本国外で発生した損害。
9. 製品を修理するため、第三者に委託して「搬送中」に発生した損害。
10. 弊社よりの購入者または直接のお届け先以外の場合。
11. 保証書を紛失した場合。
※詳しくは弊社HPにて保証規約を御確認ください。

【制作について】
各項目は見出しのサイズで大きく、細かい細則はかなり細かい字で構いません。
上記の内下記のところは弊社で個別に印字をしますので、入力スペースをお願い
します。

保証番号

受注番号

お買い上げ日時

購入者氏名

購入者住所

上記の希望する色、赤青については無視して頂いて結構です。
保証番号などの後から出力する部分をしっかり空けといてく
ださると助かります。
細かい条件は読めるか読めない程度で構いません。

全体の色合いとバランス、安心感と砕け感の調和が秀逸でした。
提案者も連絡がみつで信頼のおける方でした。

提案してくれたミルダーの方々有難うございました。
おかげさまで良い保証書ができて満足しております。
今後もまた何か依頼をしますので、よろしくお願い致します。

```html
<!DOCTYPE html>
<html lang="ja">
<head>
<meta charset="utf-8">
<title>人形修理保証書</title>
<link href="https://fonts.googleapis.com/css2?family=Noto+Serif+JP:wght@400;600;700;900&family=Noto+Sans+JP:wght@400;500;700&display=swap" rel="stylesheet">
<style>
  :root{
    --paper:#ffffff;
    --navy:#2b3f86;
    --navy-soft:#4a5fa6;
    --frame-a:#3d56a3;
    --frame-b:#8fa3d6;
    --ground-a:#f3f5fb;
    --ground-b:#e6ebf6;
    --ink:#222631;
    --accent:#c2304a;
    --rule:#b7c2e0;
    --seal:#c8272f;
    --field-bg:#ffffff;
  }
  *{box-sizing:border-box;margin:0;padding:0}
  html,body{width:876px;height:1200px;overflow:hidden;background:var(--paper)}
  body{font-family:"Noto Sans JP",sans-serif;color:var(--ink);position:relative}
  .certificate{position:absolute;left:88px;top:66px;width:702px;height:1098px}
  .frame-pattern{position:absolute;inset:0;background:linear-gradient(135deg,var(--frame-a),var(--frame-b) 50%,var(--frame-a));}
  .frame-line{position:absolute;inset:18px;border:2px solid var(--paper);}
  .ground{position:absolute;inset:24px;background:linear-gradient(180deg,var(--ground-a),var(--ground-b));}
  .content{position:absolute;inset:24px;padding:30px 34px 0}
  .title{font-family:"Noto Serif JP",serif;font-weight:900;font-size:42px;letter-spacing:.12em;text-align:center;color:var(--navy);line-height:1.3}
  .title-rule{height:3px;background:var(--navy);margin:10px 0 14px}
  .intro{font-weight:700;font-size:15px;line-height:1.7;letter-spacing:.02em}
  .section-head{font-family:"Noto Serif JP",serif;font-weight:700;font-size:20px;color:var(--navy);margin-top:18px;display:flex;align-items:baseline;gap:28px;line-height:1.4}
  .section-head .term{font-family:"Noto Sans JP",sans-serif;font-size:15px;color:var(--ink);font-weight:700}
  .section-rule{height:1px;background:var(--rule);margin-top:5px}
  .coverage{display:flex;gap:20px;margin-top:10px}
  .coverage-text{width:236px;font-size:11.5px;line-height:1.7}
  .coverage-text .item{margin-top:4px}
  .rate-table{flex:1}
  .rate-title{font-size:14px;color:var(--accent);font-weight:700}
  .rate-note{font-size:9px;color:var(--accent);margin:2px 0 5px}
  .rate-row{display:flex;justify-content:space-between;font-size:12px;padding:6px 6px;border-bottom:1px solid var(--rule)}
  .rate-row:nth-child(odd){background:rgba(255,255,255,.7)}
  .exclusions{font-size:10.5px;line-height:1.7;margin-top:8px}
  .exclusions .note{color:var(--navy-soft)}
  .entry-fields{margin-top:14px;display:grid;grid-template-columns:1fr 1fr;border:1px solid var(--navy);background:var(--field-bg)}
  .field{display:flex;align-items:stretch;height:38px;border-bottom:1px solid var(--rule)}
  .field:nth-child(odd){border-right:1px solid var(--rule)}
  .field.wide{grid-column:1 / 3;border-right:none;border-bottom:none;height:42px}
  .field-label{width:112px;flex:none;display:flex;align-items:center;justify-content:center;font-size:12px;font-weight:700;color:var(--paper);background:var(--navy-soft)}
  .field-blank{flex:1}
  .footer{position:absolute;left:34px;right:34px;bottom:34px;display:flex;align-items:flex-end;justify-content:space-between}
  .shop-name{display:flex;align-items:center;gap:8px;font-weight:700;font-size:15px;color:var(--navy)}
  .shop-name .dot{width:14px;height:14px;border-radius:50%;background:var(--navy)}
  .company{font-family:"Noto Serif JP",serif;font-weight:700;font-size:30px;letter-spacing:.14em;color:var(--ink);line-height:1.2}
  .company small{font-size:17px;letter-spacing:.05em;margin-right:10px}
  .seal{width:74px;height:74px;background:var(--seal);border-radius:4px}
</style>
</head>
<body>
  <div class="certificate">
    <div class="frame-pattern" role="img" aria-label="保証書の装飾枠（青系の地紋模様）"></div>
    <div class="frame-line"></div>
    <div class="ground" role="img" aria-label="淡い青の地紋"></div>
    <div class="content">
      <h1 class="title">人形修理保証書</h1>
      <div class="title-rule"></div>
      <p class="intro">お買い上げの御人形はお客様に十分ご満足いただけますよう細心の注意を払っております。万一、人形に不具合が生じましたら下記の条件に従って保証いたします。</p>

      <h2 class="section-head">1 修理保証期間 <span class="term">ご購入日より５年間</span></h2>
      <div class="section-rule"></div>

      <h2 class="section-head">2 保証内容</h2>
      <div class="section-rule"></div>
      <div class="coverage">
        <div class="coverage-text">
          <p>保証期間中、日本国内で正常な使用で過失なく人形本体部分（お顔、髪の毛、胴体、手足、人形の持ち物道具）に不具合が生じた場合最大2回まで下記の割合で費用保証します。</p>
          <p class="item">a. 対象商品が修理可能な場合……下記に定める割合と額を限度とした修理費用</p>
          <p class="item">b. 対象商品が修理不可能な場合……下記に基づく限度額の代替品の提供を保証</p>
        </div>
        <div class="rate-table">
          <p class="rate-title">人形修理保証・補償割合</p>
          <p class="rate-note">（保証限度額はいずれも実質購入金額を上限とします）</p>
          <div class="rate-rows">
            <div class="rate-row"><span>購入日より1年未満</span><span>修理金額（税別）の100%</span></div>
            <div class="rate-row"><span>購入日より1年以上2年未満</span><span>修理金額（税別）の50%</span></div>
            <div class="rate-row"><span>購入日より2年以上3年未満</span><span>修理金額（税別）の40%</span></div>
            <div class="rate-row"><span>購入日より3年以上4年未満</span><span>修理金額（税別）の30%</span></div>
            <div class="rate-row"><span>購入日より4年以上5年未満</span><span>修理金額（税別）の20%</span></div>
          </div>
        </div>
      </div>

      <h2 class="section-head">3 保証適用除外事項項目</h2>
      <div class="section-rule"></div>
      <p class="exclusions">1. 保証期間を過ぎて発生した損害。2. 故意や重過失、差押えによる損害。3. 火事、地震、洪水、津波などの天災による損害。4. 水濡れや湿気、カビ等による保管状況による劣化の損害。5. 錆、変色、擦傷、劣化等、通常の使用による自然消耗で発生した損害。6.「付属品」（ガラスケース、お道具、飾り台、屏風、親王台、お花、芯木など人形自体以外の、付属品または構成品に分けられる部分）に生じた損害。7. 製品を無断で改造もしくは修理したことが原因となって生じた損害。8. 日本国外で発生した損害。9. 製品を修理するため、第三者に委託して「搬送中」に発生した損害。10. 弊社よりの購入者または直接のお届け先以外の場合。11. 保証書を紛失した場合。<br><span class="note">※詳しくは弊社HPにて保証規約を御確認ください。</span></p>

      <div class="entry-fields">
        <div class="field"><span class="field-label">保証番号</span><span class="field-blank"></span></div>
        <div class="field"><span class="field-label">受注番号</span><span class="field-blank"></span></div>
        <div class="field"><span class="field-label">お買い上げ日時</span><span class="field-blank"></span></div>
        <div class="field"><span class="field-label">購入者氏名</span><span class="field-blank"></span></div>
        <div class="field wide"><span class="field-label">購入者住所</span><span class="field-blank"></span></div>
      </div>

      <div class="footer">
        <div class="shop-name"><span class="dot"></span>飾り処サクヤ</div>
        <div class="company"><small>株式会社</small>樫井</div>
        <div class="seal" role="img" aria-label="社印（角印）"></div>
      </div>
    </div>
  </div>
</body>
</html>
```